Vintrell Power Point Presentation

We need our presentation designed. Our current presentation is inconsistent, too text heavy, and complicated. We want this to be clean, sleek, and impressive as our references attached are.

Our colors are blue, black, and white.
Our font is roboto.

```html
<!DOCTYPE html>
<html lang="en">
<head>
<meta charset="utf-8">
<title>Vintrell Presentation</title>
<link href="https://fonts.googleapis.com/css2?family=Roboto:wght@400;500;700;900&display=swap" rel="stylesheet">
<style>
:root{
  --blue:#1a7cf5;
  --blue-dark:#0b5fd8;
  --ink:#111418;
  --text:#3a3f47;
  --muted:#6b7280;
  --white:#ffffff;
  --page:#d6d8db;
  --card-shadow:0 2px 6px rgba(20,40,80,.12);
}
*{margin:0;padding:0;box-sizing:border-box}
html,body{width:807px;height:1200px;overflow:hidden;background:var(--page);font-family:'Roboto',sans-serif;color:var(--text)}
.sheet{position:absolute;left:0;top:0;width:1568px;height:2333px;transform:scale(.5147);transform-origin:0 0}
.slide{position:absolute;width:663px;height:373px;background:var(--white);overflow:hidden}
.abs{position:absolute}
.brand{position:absolute;display:flex;align-items:center;gap:5px;font-size:17px;font-weight:500;color:var(--blue)}
.brand .mark{width:20px;height:20px;border-radius:4px;background:var(--blue)}
.brand.light{color:var(--white)}
.brand.light .mark{background:var(--white)}
.heading{position:absolute;left:40px;top:22px;display:flex;align-items:center;gap:14px;font-size:23px;font-weight:700;color:var(--ink);letter-spacing:.3px}
.heading::before{content:"";width:6px;height:27px;background:var(--blue)}
.lede{position:absolute;left:40px;top:62px;font-size:8px;line-height:14px;color:var(--text);width:290px}
.btn{position:absolute;width:177px;height:35px;background:var(--blue);color:var(--white);font-size:10px;font-weight:500;display:flex;align-items:center;justify-content:center}
.card{position:absolute;width:177px;height:37px;background:var(--white);box-shadow:var(--card-shadow);display:flex;align-items:center;gap:8px;padding:0 8px;font-size:8px;line-height:13px;color:var(--text)}
.card svg{flex:none;width:20px;height:20px}
.stat{position:absolute;width:90px}
.stat b{display:block;font-size:14px;font-weight:700;color:var(--blue);margin-bottom:6px}
.stat span{font-size:8px;line-height:12px;color:var(--text)}
.partner{position:absolute;font-size:9px;font-weight:700;color:var(--ink)}
.adv{position:absolute;width:56px;height:56px;border-radius:50%;background:var(--white);box-shadow:0 3px 8px rgba(20,40,80,.18);display:flex;align-items:center;justify-content:center;font-size:8px;font-weight:700;color:var(--blue);text-align:center;line-height:10px}
.ticks{list-style:none;position:absolute}
.ticks li{position:relative;padding-left:16px;font-size:8px;line-height:14px;color:var(--text)}
.ticks li::before{content:"";position:absolute;left:0;top:3px;width:7px;height:7px;border-radius:50%;background:var(--blue)}
.spec{position:absolute;top:118px;width:177px;height:230px;border:1.5px solid var(--blue);border-top:none;border-radius:0 0 3px 3px}
.spec .pill{position:absolute;left:10px;top:-18px;width:155px;height:35px;border-radius:18px;background:var(--blue);color:var(--white);font-size:10px;font-weight:700;display:flex;align-items:center;justify-content:center}
.spec .ticks{left:16px;top:40px;width:150px}
.spec .ticks li{margin-bottom:9px}
.photo{position:absolute}
</style>
</head>
<body>
<main class="sheet">

  <!-- Cover -->
  <section class="slide" style="left:93px;top:107px">
    <svg class="abs" width="663" height="373" style="left:0;top:0">
      <path d="M0 0H420Q440 0 433 20L358 355Q354 373 335 373H0Z" fill="var(--blue)"/>
    </svg>
    <svg class="abs" width="663" height="373" style="left:0;top:0" role="img" aria-label="Photos of indoor venues with wall-mounted screens">
      <defs>
        <linearGradient id="ph1" x1="0" y1="0" x2="1" y2="1"><stop offset="0" stop-color="#d8d6d0"/><stop offset="1" stop-color="#8d8a84"/></linearGradient>
        <linearGradient id="ph2" x1="0" y1="0" x2="1" y2="1"><stop offset="0" stop-color="#c9b79b"/><stop offset="1" stop-color="#6f5c45"/></linearGradient>
        <linearGradient id="ph3" x1="0" y1="0" x2="1" y2="1"><stop offset="0" stop-color="#8a4a30"/><stop offset="1" stop-color="#3a2a24"/></linearGradient>
      </defs>
      <path d="M470 0H663V100Q660 118 645 120H445Z" fill="url(#ph1)"/>
      <path d="M435 128H632L608 246H410Z" fill="url(#ph2)"/>
      <path d="M400 254H602L575 373H382Z" fill="url(#ph3)"/>
    </svg>
    <div class="brand light" style="left:40px;top:32px"><span class="mark"></span>Vintrell</div>
    <h1 class="abs" style="left:38px;top:133px;font-size:27px;line-height:31px;font-weight:700;color:var(--white)">Indoor DOOH Audiences<br>at Scale</h1>
    <div class="abs" style="left:40px;top:210px;width:70px;height:2px;background:rgba(255,255,255,.45)"></div>
    <div class="abs" style="left:40px;top:251px;font-size:12px;font-weight:700;color:var(--white);text-decoration:underline">BUY ON VINTRELL ➔</div>
    <div class="abs" style="left:205px;top:251px;font-size:11px;color:var(--white)">✉&nbsp; info@vintrell.com</div>
  </section>

  <!-- Why go indoor -->
  <section class="slide" style="left:812px;top:107px">
    <h2 class="heading">WHY GO INDOOR</h2>
    <div class="brand" style="left:533px;top:27px"><span class="mark"></span>Vintrell</div>
    <p class="lede">it's not just lockdowns ending - recent uptick has been driven by the unique effectiveness of indoor DOOH ad exposure.</p>
    <div class="btn" style="left:40px;top:107px">It's special...</div>
    <div class="btn" style="left:243px;top:107px">It's powerful...</div>
    <div class="btn" style="left:446px;top:107px">It's special...</div>
    <div class="card" style="left:40px;top:163px"><svg viewBox="0 0 20 20"><circle cx="10" cy="11" r="7" fill="none" stroke="var(--blue)" stroke-width="1.3"/><path d="M10 7v4l3 2" stroke="var(--blue)" fill="none" stroke-width="1.3"/></svg>Dwell time measured in minutes, not seconds</div>
    <div class="card" style="left:40px;top:212px"><svg viewBox="0 0 20 20"><path d="M10 2l7 3v5c0 4-3 7-7 8-4-1-7-4-7-8V5z" fill="none" stroke="var(--blue)" stroke-width="1.3"/></svg>Brand-safe</div>
    <div class="card" style="left:40px;top:260px"><svg viewBox="0 0 20 20"><rect x="3" y="4" width="14" height="10" fill="none" stroke="var(--blue)" stroke-width="1.3"/><path d="M7 17h6" stroke="var(--blue)" stroke-width="1.3"/></svg>100% viewability by humans, not bots</div>
    <div class="card" style="left:40px;top:308px"><svg viewBox="0 0 20 20"><rect x="2" y="3" width="16" height="14" fill="none" stroke="var(--blue)" stroke-width="1.3"/><path d="M6 7l3 3-3 3M10 7l3 3-3 3" stroke="var(--blue)" fill="none" stroke-width="1.3"/></svg>Not Skippable</div>
    <div class="card" style="left:243px;top:163px"><svg viewBox="0 0 20 20"><rect x="2" y="4" width="16" height="11" fill="none" stroke="var(--blue)" stroke-width="1.3"/><path d="M5 12l3-3 3 2 4-4" stroke="var(--blue)" fill="none" stroke-width="1.3"/></svg>Engaged impressions, consumer attention, means...</div>
    <div class="card" style="left:243px;top:212px"><svg viewBox="0 0 20 20"><circle cx="10" cy="10" r="7" fill="none" stroke="var(--blue)" stroke-width="1.3"/><circle cx="10" cy="10" r="3" fill="none" stroke="var(--blue)" stroke-width="1.3"/></svg>Indoor DOOH 2x more likely to be seen, recalled, than traditional</div>
    <div class="card" style="left:446px;top:163px"><svg viewBox="0 0 20 20"><path d="M16 8a6 6 0 0 0-11-2M4 12a6 6 0 0 0 11 2" stroke="var(--blue)" fill="none" stroke-width="1.4"/><path d="M5 3v3h3M15 17v-3h-3" stroke="var(--blue)" fill="none" stroke-width="1.4"/></svg>2x increase in reach if added to Omni -Channel campaigns</div>
  </section>

  <!-- Statement -->
  <section class="slide" style="left:93px;top:547px">
    <svg class="abs" width="663" height="373" style="left:0;top:0">
      <path d="M0 0H648Q663 0 660 15L590 355Q585 373 565 373H0Z" fill="var(--blue)"/>
    </svg>
    <div class="brand light" style="left:40px;top:32px"><span class="mark"></span>Vintrell</div>
    <p class="abs" style="left:38px;top:137px;width:520px;font-size:19px;line-height:31px;color:var(--white);font-weight:400">Vintrell offers advertisers easy, affordable access to <b>North America's largest indoor DOOH network,</b> containing <b>diverse audience segments</b> while <b>captivated in indoor environments</b></p>
  </section>

  <!-- Network -->
  <section class="slide" style="left:812px;top:547px">
    <svg class="photo" width="663" height="373" style="left:0;top:0" role="img" aria-label="Photo of a person looking at an indoor digital screen">
      <defs><linearGradient id="ph4" x1="0" y1="0" x2="1" y2="1"><stop offset="0" stop-color="#e9edf0"/><stop offset=".6" stop-color="#9fb0ba"/><stop offset="1" stop-color="#2c3a44"/></linearGradient></defs>
      <path d="M388 0H663V373H470Q452 373 450 355L373 15Q370 0 388 0Z" fill="url(#ph4)"/>
    </svg>
    <h2 class="heading">NETWORK</h2>
    <p class="lede">Vintrell is your DOOH partner, connecting your partners and advertisers to a nation-wide network of premium, place-based screens.</p>
    <div class="abs" style="left:40px;top:110px;font-size:9px;font-weight:700;color:var(--ink)">Our nationwide network.</div>
    <div class="abs" role="img" aria-label="Map of network locations across the United States" style="left:40px;top:136px;width:155px;height:80px;background:linear-gradient(135deg,#c7ccd3,#dfe3e8);border-radius:10px 30px 20px 15px"></div>
    <div class="abs" role="img" aria-label="Map of network locations across Canada" style="left:225px;top:130px;width:158px;height:90px;background:linear-gradient(135deg,#dfe2e6,#c9cdd3);border-radius:20px 10px 30px 10px"></div>
    <div class="stat" style="left:40px;top:253px"><b>12B+</b><span>Impressions<br>Annually</span></div>
    <div class="stat" style="left:134px;top:253px"><b>50+</b><span>DMA's</span></div>
    <div class="stat" style="left:229px;top:253px"><b>26,105+</b><span>Venues</span></div>
    <div class="stat" style="left:323px;top:253px"><b>31,594+</b><span>Screens</span></div>
    <div class="stat" style="left:40px;top:314px"><b>12000+</b><span>Retail<br>screens</span></div>
    <div class="stat" style="left:134px;top:314px"><b>16000+</b><span>Restobar screens</span></div>
    <div class="stat" style="left:229px;top:314px"><b>2000+</b><span>Medical screens</span></div>
    <div class="stat" style="left:323px;top:314px"><b>4000+</b><span>Grocery screens</span></div>
  </section>

  <!-- How to buy -->
  <section class="slide" style="left:93px;top:987px">
    <h2 class="heading">HOW TO BUY</h2>
    <div class="brand" style="left:533px;top:27px"><span class="mark"></span>Vintrell</div>
    <p class="lede">Vintrell's network and unique audiences are accessible however you buy your media.</p>
    <div class="btn" style="left:40px;top:107px">Audiences...</div>
    <div class="btn" style="left:243px;top:107px">...you can buy anywhere...</div>
    <div class="btn" style="left:446px;top:107px">...however you'd like.</div>
    <div class="card" style="left:40px;top:163px"><svg viewBox="0 0 20 20"><circle cx="8" cy="9" r="5" fill="none" stroke="var(--blue)" stroke-width="1.3"/><path d="M8 6v6" stroke="var(--blue)" stroke-width="1.3"/></svg>High net worth</div>
    <div class="card" style="left:40px;top:212px"><svg viewBox="0 0 20 20"><rect x="2" y="5" width="16" height="10" fill="none" stroke="var(--blue)" stroke-width="1.3"/><path d="M10 5v10" stroke="var(--blue)" stroke-width="1.3"/><circle cx="10" cy="10" r="2" fill="none" stroke="var(--blue)"/></svg>Sports Fans</div>
    <div class="card" style="left:40px;top:260px"><svg viewBox="0 0 20 20"><circle cx="9" cy="4" r="2" fill="none" stroke="var(--blue)" stroke-width="1.3"/><path d="M9 7v5l4 5M9 12l-4 5" stroke="var(--blue)" fill="none" stroke-width="1.3"/></svg>High dwell time</div>
    <div class="partner" style="left:248px;top:171px">Mediaform</div>
    <div class="partner" style="left:305px;top:171px;font-size:7px">tradeloft</div>
    <div class="partner" style="left:372px;top:169px;font-size:10px;color:var(--muted)">ubiqo</div>
    <div class="partner" style="left:248px;top:196px;color:#1aa36b">OutRoute</div>
    <div class="partner" style="left:305px;top:195px;color:var(--blue)">campfield</div>
    <div class="partner" style="left:372px;top:195px">aterra</div>
    <div class="partner" style="left:248px;top:222px;font-size:7px;color:#b0207a">Hivegrid</div>
    <div class="partner" style="left:300px;top:222px;font-size:7px">pulsenode</div>
    <div class="partner" style="left:355px;top:222px;font-size:7px;color:#c0392b">Adorna</div>
    <div class="partner" style="left:390px;top:222px;font-size:7px">veranto media</div>
    <div class="card" style="left:446px;top:163px"><svg viewBox="0 0 20 20"><path d="M3 15l5-9 4 5 5-7" stroke="var(--blue)" fill="none" stroke-width="1.3"/></svg>Direct Buying</div>
    <div class="card" style="left:446px;top:212px"><svg viewBox="0 0 20 20"><circle cx="10" cy="10" r="2" fill="none" stroke="var(--blue)" stroke-width="1.3"/><circle cx="3" cy="3" r="1.5" fill="var(--blue)"/><circle cx="17" cy="3" r="1.5" fill="var(--blue)"/><circle cx="3" cy="17" r="1.5" fill="var(--blue)"/><circle cx="17" cy="17" r="1.5" fill="var(--blue)"/><path d="M4 4l5 5M16 4l-5 5M4 16l5-5M16 16l-5-5" stroke="var(--blue)"/></svg>Open RTB</div>
    <div class="card" style="left:446px;top:260px"><svg viewBox="0 0 20 20"><rect x="3" y="3" width="11" height="14" fill="none" stroke="var(--blue)" stroke-width="1.3"/><path d="M6 7h5M6 10h5M6 13h3" stroke="var(--blue)"/></svg>Programmatic Guaranteed or PMP</div>
  </section>

  <!-- Advertisers -->
  <section class="slide" style="left:812px;top:987px">
    <h2 class="heading">ADVERTISERS</h2>
    <div class="brand" style="left:533px;top:27px"><span class="mark"></span>Vintrell</div>
    <p class="lede">Brands that buy on our network.</p>
    <div class="adv" style="left:41px;top:107px">Northbank</div>
    <div class="adv" style="left:146px;top:107px">Starlane</div>
    <div class="adv" style="left:252px;top:107px">Maplefizz</div>
    <div class="adv" style="left:357px;top:107px">Hemvik</div>
    <div class="adv" style="left:462px;top:107px">Marceau</div>
    <div class="adv" style="left:568px;top:107px">DashDrop</div>
    <div class="adv" style="left:41px;top:197px">Candibits</div>
    <div class="adv" style="left:146px;top:197px">Fenwick</div>
    <div class="adv" style="left:252px;top:197px">Pixolo</div>
    <div class="adv" style="left:357px;top:197px">Goldarch</div>
    <div class="adv" style="left:462px;top:197px">IceLeague</div>
    <div class="adv" style="left:568px;top:197px">Paycircle</div>
    <div class="adv" style="left:146px;top:287px">Hoagie Co</div>
    <div class="adv" style="left:252px;top:287px">Clearwave</div>
    <div class="adv" style="left:357px;top:287px">Orvane</div>
    <div class="adv" style="left:462px;top:287px">Tunely</div>
  </section>

  <!-- Key takeaways -->
  <section class="slide" style="left:93px;top:1427px">
    <svg class="photo" width="663" height="373" style="left:0;top:0" role="img" aria-label="Photo of a clinic waiting-room screen showing a flu vaccine message">
      <defs><linearGradient id="ph5" x1="0" y1="0" x2="1" y2="1"><stop offset="0" stop-color="#d9cbb4"/><stop offset=".5" stop-color="#b49c7b"/><stop offset="1" stop-color="#7a644a"/></linearGradient></defs>
      <path d="M395 0H663V373H300Q292 373 295 360L378 15Q382 0 395 0Z" fill="url(#ph5)"/>
      <rect x="365" y="75" width="232" height="140" fill="#1c1f24"/>
      <rect x="372" y="82" width="218" height="126" fill="#5d7a93"/>
    </svg>
    <h2 class="heading">VINTRELL Key Takeaways</h2>
    <ul class="ticks" style="left:40px;top:106px;width:270px">
      <li style="margin-bottom:10px">North America's largest and fastest-growing indoor DOOH screen network</li>
      <li style="margin-bottom:10px">Powerful enough to capture the attention of nationwide audiences at scale, specific enough to provide access to diverse audience segments</li>
      <li style="margin-bottom:10px">Programmatically-accessible, ensuring cost-efficiency, transparency and real-time optimizations</li>
      <li>Flexible enough to get any DOOH campaign or integration up and running quickly and without issue</li>
    </ul>
    <div class="brand" style="left:40px;top:320px"><span class="mark"></span>Vintrell</div>
  </section>

  <!-- Formats -->
  <section class="slide" style="left:812px;top:1427px">
    <h2 class="heading">DIGITAL MEDIA FORMATS</h2>
    <div class="brand" style="left:533px;top:27px"><span class="mark"></span>Vintrell</div>
    <div class="abs" style="left:40px;top:62px;font-size:10px;font-weight:500;color:var(--ink)">Specifications</div>
    <div class="spec" style="left:40px"><div class="pill">Network</div>
      <ul class="ticks"><li>Indoor, 32 –73" Screens</li><li>Full Screen Take Over</li><li>Sold programmatically</li><li>No Blacklisted Advertisers</li><li>Approval Upon Venue Review</li></ul></div>
    <div class="spec" style="left:243px"><div class="pill">Content Specifications</div>
      <ul class="ticks"><li>1920 pixels (w) x 1080 pixels (h) 16:9</li><li>1080 pixels (w) x 1920 pixels (h) 9:16</li><li>Static: PNG, RGB, encoded. JPG or H.264</li><li>Video: .MP$ / encoded .MOV</li><li>Will repurpose TV spots, banner ads; transcode ill-fitting static creatives</li></ul></div>
    <div class="spec" style="left:446px"><div class="pill">Ad Content Play Suggestions</div>
      <ul class="ticks"><li>15 second</li><li>30 second</li><li>60 second</li></ul></div>
  </section>

  <!-- Closing -->
  <section class="slide" style="left:453px;top:1867px;background:linear-gradient(180deg,#1f6ff0 0%,#1867e6 55%,#2b78ee 100%)">
    <div class="brand light" style="left:250px;top:148px;font-size:32px;gap:10px"><span class="mark" style="width:38px;height:38px;border-radius:7px"></span>Vintrell</div>
    <div class="abs" style="left:0;top:218px;width:663px;text-align:center;font-size:10px;color:var(--white)">◉ https://vintrell.com/ &nbsp;&nbsp;|&nbsp;&nbsp; ☏ +1 800-555-0142 &nbsp;&nbsp;|&nbsp;&nbsp; ✉ info@vintrell.com</div>
  </section>

</main>
</body>
</html>
```